Need a website to promote and sell my book

Using images from the book, I need a website designed that helps promote the book and eventually sell it.
*Need a landing page
*About the author page
*Storefront page to purchase
*Coming soon page
*"Featured in" page that can link to news articles etc.
The images posted here are examples, the winner of the contest will get the images from the finished book. I will provide the exact text to the winner of the contest.

I can also provide images of kids reading the book. For now, I'll just use one, the winner can have them all to choose from.
Updates

Extending deadline to allow for a few more designers to submit and to allow time for me to review and hold a poll

Target Market(s)

Parents, aunts, uncles, grandparents, friends who have kids; teachers, daycare teachers, babysitters etc.

Industry/Entity Type

Custom Publishing

Coding

Coded - Design and coding required

Number of Pages Required

5+ page

Font styles to use
Sans Serif

Colors

Designer to choose colors to be used in the design.

Requirements
Must have
• It must have a fun feel like the book.
Nice to have
• Would be great to have a section that automatically pulls tweets about the book into it.

```html
<!DOCTYPE html>
<html lang="en">
<head>
<meta charset="utf-8">
<title>Little Lab Adventures</title>
<link href="https://fonts.googleapis.com/css2?family=Baloo+2:wght@700;800&family=Rubik:wght@400;500;700&display=swap" rel="stylesheet">
<style>
:root{
  --navy:#1c2947;
  --navy-deep:#17223c;
  --red:#d8102f;
  --teal:#2fcbbf;
  --green:#23b06d;
  --plum:#3c3a78;
  --yellow:#f8ad06;
  --light:#f6f6f6;
  --ink:#3d3d4a;
  --pink:#ff5b7f;
  --white:#ffffff;
}
*{margin:0;padding:0;box-sizing:border-box}
html,body{width:1200px;height:3809px;overflow:hidden}
body{position:relative;font-family:"Rubik",sans-serif;background:var(--light);color:var(--ink)}
.abs{position:absolute}
.display{font-family:"Baloo 2",sans-serif;font-weight:800}
.btn{position:absolute;display:flex;align-items:center;justify-content:center;border-radius:30px;color:var(--white);font-family:"Rubik",sans-serif;font-weight:700;text-decoration:none}
.wave{position:absolute}
.brand-circle{position:absolute;background:var(--white);border-radius:50%;display:flex;align-items:center;justify-content:center;text-align:center;font-family:"Rubik",sans-serif;font-weight:500;color:var(--red);line-height:1.05}

/* hero */
.hero{position:absolute;left:0;top:0;width:1200px;height:596px;background:var(--navy)}
.topbar{position:absolute;left:0;top:0;width:1200px;height:7px;background:var(--red)}
.nav{position:absolute;top:52px;left:365px}
.nav a{color:var(--white);font-size:14px;font-weight:500;text-decoration:none;position:absolute;white-space:nowrap}
.social-top{position:absolute;top:42px;width:44px;height:44px;border-radius:50%;background:#35415d}
.hero-title{position:absolute;left:57px;top:180px;width:660px;font-size:56px;line-height:54px;color:var(--white)}
.hero-copy{position:absolute;left:67px;top:323px;width:500px;font-size:13.5px;line-height:26px;color:#8fa0c8}
.book-cover{position:absolute;left:743px;top:167px;width:332px;height:466px;background:linear-gradient(180deg,#7fd3e8 0%,#8fd8ea 55%,#f2c15f 100%);box-shadow:8px 10px 18px rgba(0,0,0,.25)}
.badge{position:absolute;left:424px;top:525px;width:167px;height:115px;border-radius:60px;background:linear-gradient(135deg,#ff5aa0,#f04b8c)}

/* teal */
.teal-band{position:absolute;left:0;top:596px;width:1200px;height:700px;background:var(--teal)}
.author-art{position:absolute;left:650px;top:650px;width:222px;height:188px;border-radius:110px 110px 0 0;background:linear-gradient(180deg,#c9704a,#e7c7a3)}
.lab-art{position:absolute;left:148px;top:760px;width:145px;height:75px;border-radius:20px;background:linear-gradient(135deg,#e5c37e,#f26a52)}
.message{position:absolute;left:103px;top:838px;width:992px;height:340px;background:var(--white);border-radius:34px;box-shadow:0 6px 0 rgba(0,0,0,.06)}
.message-title{position:absolute;left:65px;top:78px;width:260px;font-family:"Rubik",sans-serif;font-weight:700;font-size:31px;line-height:38px;color:var(--plum)}
.message .more{position:absolute;left:65px;top:203px;font-size:14px;font-weight:700;color:#1f4c3e;text-decoration:none}
.message .copy{position:absolute;left:352px;top:46px;width:540px;font-size:13.5px;line-height:28px;color:var(--ink)}

/* play */
.play-band{position:absolute;left:0;top:1228px;width:1200px;height:551px;background:var(--green)}
.comic{position:absolute;background:#f7a963;border:6px solid var(--white);box-shadow:0 4px 10px rgba(0,0,0,.15)}
.play-title{position:absolute;left:727px;top:1350px;font-size:46px;line-height:60px;color:var(--white)}
.play-copy{position:absolute;left:728px;top:1433px;width:380px;font-size:13.5px;line-height:28px;color:var(--white);font-weight:500}
.flask-art{position:absolute;left:925px;top:1568px;width:168px;height:108px;border-radius:16px;background:linear-gradient(135deg,#7fdca7,#e4535b)}

/* gallery */
.kicker{position:absolute;left:0;width:1200px;top:1823px;text-align:center;font-size:12px;color:var(--pink)}
.gallery-title{position:absolute;left:0;width:1200px;top:1840px;text-align:center;font-size:44px;line-height:56px;color:var(--plum)}
.photo{position:absolute;top:1955px;width:214px;height:241px}

/* articles */
.articles-band{position:absolute;left:0;top:2350px;width:1200px;height:920px;background:var(--teal)}
.articles-title{position:absolute;left:0;width:1200px;top:2460px;text-align:center;font-size:58px;line-height:70px;color:var(--plum)}
.card{position:absolute;background:#f8f3ea;border-radius:8px;overflow:hidden}
.card .art{width:100%;height:243px}
.card h3{position:absolute;left:55px;top:328px;width:300px;font-family:"Rubik",sans-serif;font-weight:700;font-size:20px;line-height:28px;color:var(--plum)}
.card p{position:absolute;left:55px;width:290px;font-size:10.5px;line-height:20px;color:#8a8a95}
.card .read{position:absolute;left:55px;width:125px;height:40px;border-radius:20px;background:var(--yellow);color:var(--white);font-size:10px;font-weight:700;display:flex;align-items:center;justify-content:center}
.faded{opacity:.35}
.dot{position:absolute;top:3190px;width:22px;height:20px;border-radius:50%}

/* footer */
.footer{position:absolute;left:0;top:3269px;width:1200px;height:540px;background:var(--navy-deep)}
.footer-head{position:absolute;top:3350px;font-size:20px;color:var(--white);font-family:"Rubik",sans-serif;font-weight:700}
.footer-text{position:absolute;font-size:13px;line-height:26px;color:#c9d0e2}
.foot-link{position:absolute;left:646px;font-size:13px;color:#c9d0e2}
.email{position:absolute;left:903px;top:3417px;width:237px;height:59px;border-radius:12px;background:var(--white);font-size:12.5px;color:#777;display:flex;align-items:center;padding-left:34px}
.foot-social{position:absolute;top:3694px;width:50px;height:50px;border-radius:50%}
.copyright{position:absolute;left:0;width:1200px;top:3766px;text-align:center;font-size:12.5px;color:#c9d0e2}
</style>
</head>
<body>

<!-- hero -->
<section class="hero">
  <div class="topbar"></div>
  <div class="brand-circle" style="left:41px;top:-30px;width:130px;height:128px;font-size:17px;padding-top:26px">Little Lab<br>Adventures</div>
  <nav class="nav">
    <a href="#" style="left:0">Home</a>
    <a href="#" style="left:107px">About Author</a>
    <a href="#" style="left:253px">Shop</a>
    <a href="#" style="left:346px">Gallery</a>
    <a href="#" style="left:443px">Upcoming</a>
    <a href="#" style="left:568px">Contact</a>
  </nav>
  <svg class="wave" style="left:360px;top:73px" width="54" height="8" viewBox="0 0 54 8"><path d="M1 4 Q5 0 9 4 T17 4 T25 4 T33 4 T41 4 T49 4 T53 4" fill="none" stroke="var(--pink)" stroke-width="1.6"/></svg>
  <div class="social-top" style="left:1030px" role="img" aria-label="Social link"></div>
  <div class="social-top" style="left:1083px" role="img" aria-label="Social link"></div>
  <div class="social-top" style="left:1136px" role="img" aria-label="Social link"></div>
  <h1 class="display hero-title">Best book for Your Child to Learn Chemistry</h1>
  <p class="hero-copy">There are many variations of passages of Lorem Ipsum available, but the majority have suffered alteration in some form, by injected humour, or randomised words which don't look even slightly believable you need to be sure there isn't anything embarrassing.</p>
  <a class="btn" href="#" style="left:53px;top:470px;width:145px;height:52px;background:var(--red);font-size:15px;box-shadow:0 5px 0 #9e0b22">Buy Now</a>
</section>

<!-- teal area -->
<section class="teal-band"></section>
<div class="book-cover" role="img" aria-label="Book cover illustration with four children reading"></div>
<div class="badge" role="img" aria-label="Round sticker badge with a child character"></div>
<div class="author-art" role="img" aria-label="Cartoon portrait of the author waving"></div>
<div class="lab-art" role="img" aria-label="Test tubes and an open book illustration"></div>

<div class="message">
  <h2 class="message-title">A Message from Maya</h2>
  <svg class="wave" style="left:70px;top:171px" width="54" height="8" viewBox="0 0 54 8"><path d="M1 4 Q5 0 9 4 T17 4 T25 4 T33 4 T41 4 T49 4 T53 4" fill="none" stroke="#5b7fe0" stroke-width="1.6"/></svg>
  <a class="more" href="#">More about author</a>
  <p class="copy">There are many variations of passages of Lorem Ipsum available, but the majority have suffered alteration in some form, by injected humour, or randomised words which don't look even slightly believable you need to be sure there isn't anything embarrassing.<br>There are many variations of passages of Lorem Ipsum available, but the majority have suffered alteration in some form, by injected humour, or randomised words which don't look even slightly believable you need to be sure there isn't anything embarrassing.</p>
</div>

<!-- play & learn -->
<svg class="abs" style="left:0;top:1180px" width="1200" height="80" viewBox="0 0 1200 80" role="img" aria-label="Green hillside landscape with trees">
  <path d="M0 48 Q300 30 600 42 T1200 40 V80 H0 Z" fill="var(--green)"/>
</svg>
<section class="play-band"></section>
<div class="comic" style="left:126px;top:1236px;width:285px;height:230px" role="img" aria-label="Comic panel of children learning about melting ice"></div>
<div class="comic" style="left:270px;top:1236px;width:141px;height:140px;background:#f9f9f9" role="img" aria-label="Comic speech bubble about frying an egg"></div>
<div class="comic" style="left:77px;top:1455px;width:269px;height:272px;background:#f5d2a0" role="img" aria-label="Comic panel of children comparing shoes"></div>
<div class="comic" style="left:374px;top:1377px;width:305px;height:320px" role="img" aria-label="Comic panel asking which change is different"></div>
<h2 class="display play-title">Play &amp; Learn</h2>
<p class="play-copy">There are many variations of passages of Lorem Ipsum available, but the majority have suffered alteration in some form, by injected humour, or randomised words which don't look even slightly believable you need to be sure there isn't anything embarrassing.</p>
<a class="btn" href="#" style="left:720px;top:1615px;width:183px;height:55px;background:var(--plum);font-size:15px;box-shadow:0 5px 0 #26245a">Buy Now</a>
<div class="flask-art" role="img" aria-label="Chemistry flasks and books illustration"></div>

<!-- gallery -->
<div class="kicker">Book photos</div>
<h2 class="display gallery-title">Our Gallery</h2>
<svg class="wave" style="left:578px;top:1908px" width="44" height="8" viewBox="0 0 44 8"><path d="M1 4 Q5 0 9 4 T17 4 T25 4 T33 4 T41 4" fill="none" stroke="#5b7fe0" stroke-width="1.6"/></svg>
<div class="photo" style="left:49px;background:linear-gradient(160deg,#6b6f78,#d9c4a8)" role="img" aria-label="Photo of a boy reading the book"></div>
<div class="photo" style="left:270px;background:linear-gradient(160deg,#b8b9c2,#e6d6c8)" role="img" aria-label="Photo of a girl holding the book"></div>
<div class="photo" style="left:492px;background:linear-gradient(160deg,#7a5c44,#c9b8a2)" role="img" aria-label="Photo of a child reading in a kitchen"></div>
<div class="photo" style="left:713px;background:linear-gradient(160deg,#5b4636,#cbb6a4)" role="img" aria-label="Photo of a toddler with the book"></div>
<div class="photo" style="left:935px;background:linear-gradient(160deg,#c7c7c9,#8496b8)" role="img" aria-label="Photo of a boy showing the book"></div>
<a class="btn" href="#" style="left:477px;top:2260px;width:247px;height:72px;background:var(--red);font-size:15px;border-radius:40px;box-shadow:0 5px 0 #9e0b22">More Images</a>

<!-- articles -->
<section class="articles-band"></section>
<svg class="abs" style="left:0;top:2349px" width="1200" height="60" viewBox="0 0 1200 60"><path d="M0 0 H1200 Q600 60 0 0 Z" fill="var(--light)"/></svg>
<h2 class="display articles-title">Recent Articles</h2>
<svg class="wave" style="left:578px;top:2532px" width="44" height="8" viewBox="0 0 44 8"><path d="M1 4 Q5 0 9 4 T17 4 T25 4 T33 4 T41 4" fill="none" stroke="#5b7fe0" stroke-width="1.6"/></svg>

<div class="card faded" style="left:-263px;top:2584px;width:394px;height:536px">
  <div class="art" style="background:linear-gradient(135deg,#5fa8c9,#f2b86b)" role="img" aria-label="Article illustration"></div>
  <h3>Science fun for</h3>
  <p style="top:370px">Short ideas to try at home with simple safe materials.</p>
</div>
<div class="card" style="left:166px;top:2572px;width:394px;height:576px">
  <div class="art" style="background:linear-gradient(135deg,#6cc1e6,#f4c06b)" role="img" aria-label="Illustration of children reading together"></div>
  <h3>Chemistry activities for Everyone</h3>
  <p style="top:390px">There are many people variation of passages of lorem Ipsum available in the majority sed do eius tempor incididunt ut labore et alteration in some.</p>
  <div class="read" style="top:476px">Read More</div>
</div>
<div class="card" style="left:581px;top:2572px;width:394px;height:576px">
  <div class="art" style="background:linear-gradient(135deg,#f98a2c,#f9a94b)" role="img" aria-label="Illustration of a boy with a hand lettered title"></div>
  <h3>How this book make difference in the Life of Child</h3>
  <p style="top:398px">There are many people variation of passages of lorem Ipsum available in the majority sed do eius tempor incididunt ut labore et alteration in some.</p>
  <div class="read" style="top:476px">Read More</div>
</div>
<div class="card faded" style="left:1017px;top:2584px;width:394px;height:536px">
  <div class="art" style="background:linear-gradient(135deg,#6cc1e6,#f4c06b)" role="img" aria-label="Article illustration"></div>
  <h3 style="left:40px;top:310px">How this book make difference in the Life of Child</h3>
  <p style="left:40px;top:370px">Short notes on learning and play at home.</p>
  <div class="read" style="left:40px;top:455px">Read More</div>
</div>
<div class="dot" style="left:542px;background:var(--navy)"></div>
<div class="dot" style="left:578px;background:var(--white)"></div>
<div class="dot" style="left:615px;background:var(--navy)"></div>

<!-- footer -->
<footer class="footer"></footer>
<div class="brand-circle" style="left:126px;top:3249px;width:127px;height:118px;font-size:16px">Little Lab<br>Adventures</div>
<p class="footer-text" style="left:120px;top:3387px;width:210px">Etiam rhoncus sit amet adip scing sed ipsum. Lorem ipsum dolor sit amet adipiscing sem neque.</p>
<h4 class="footer-head" style="left:359px">Contact</h4>
<svg class="abs" style="left:359px;top:3422px" width="10" height="10" viewBox="0 0 10 10"><path d="M2 1 L4 1 L5 3 L4 4 Q5 6 6 6 L7 5 L9 6 L9 8 Q8 9 7 9 Q1 8 1 2 Q1 1 2 1Z" fill="var(--pink)"/></svg>
<div class="footer-text" style="left:376px;top:3411px">555 010 0142</div>
<svg class="abs" style="left:359px;top:3475px" width="11" height="9" viewBox="0 0 11 9"><rect x="0.5" y="0.5" width="10" height="8" fill="var(--pink)"/><path d="M0.5 0.5 L5.5 5 L10.5 0.5" fill="none" stroke="var(--navy-deep)" stroke-width="1"/></svg>
<div class="footer-text" style="left:376px;top:3463px">hello@littlelabbook.com</div>
<svg class="abs" style="left:359px;top:3526px" width="10" height="11" viewBox="0 0 10 11"><path d="M5 0 A4 4 0 0 1 9 4 Q9 7 5 11 Q1 7 1 4 A4 4 0 0 1 5 0Z" fill="var(--pink)"/><circle cx="5" cy="4" r="1.5" fill="var(--navy-deep)"/></svg>
<div class="footer-text" style="left:376px;top:3515px">Address1 address2<br>Location</div>
<h4 class="footer-head" style="left:646px">Quick Links</h4>
<a class="foot-link" style="top:3416px">Home</a>
<a class="foot-link" style="top:3442px">About Author</a>
<a class="foot-link" style="top:3468px">About Book</a>
<a class="foot-link" style="top:3494px">Shop</a>
<a class="foot-link" style="top:3520px">Coming soon</a>
<a class="foot-link" style="top:3546px">Contact</a>
<h4 class="footer-head" style="left:903px">Newsletter</h4>
<div class="email">Email address</div>
<a class="btn" href="#" style="left:903px;top:3488px;width:144px;height:59px;background:var(--yellow);font-size:14px;border-radius:12px">Subscribe</a>
<div class="foot-social" style="left:543px;background:#5a4fe0" role="img" aria-label="Social link"></div>
<div class="foot-social" style="left:602px;background:#3fa6f0" role="img" aria-label="Social link"></div>
<div class="foot-social" style="left:661px;background:var(--red)" role="img" aria-label="Social link"></div>
<div class="copyright">© Copyrights, 2019 littlelabadventures.com</div>

</body>
</html>
```